one side yoga classes, other side rental log cabin

I need a flyer to advertise yoga classes on a lake , and to describe the various styles of classes, and who they can benefit, Days Times .prices
Linked to it is a rental log cabin that can be rented privetly to families or Groups (8 max) www.fernvalestays.com This also is rented to yoga teacher that would like to Hire Cabin and the Studio www.velinoshaven.co.uk or
for Holistic weekends.

Teacher

```html
<!DOCTYPE html>
<html lang="en">
<head>
<meta charset="utf-8">
<title>Velinos Haven &amp; Velinos Lodge Flyers</title>
<link rel="stylesheet" href="https://fonts.googleapis.com/css2?family=Kameron:wght@400;700&family=Oswald:wght@300;500;600&display=swap">
<style>
:root{
  --taupe:#8c8480;
  --taupe-light:#a59d98;
  --blush:#f7d8cb;
  --blush-text:#f4c8b6;
  --ink:#1f1d1c;
  --muted:#9b928d;
  --paper:#ffffff;
  --frame:#b9b4b1;
  --photo-green-dark:#2f3a1c;
  --photo-green:#6f8a34;
  --photo-brown:#5a4330;
}
*{box-sizing:border-box;margin:0;padding:0}
html,body{width:1200px;height:948px;overflow:hidden;background:var(--paper)}
.sheet{position:relative;width:950px;height:750px;transform:scale(1.2632);transform-origin:0 0}
.flyer{position:absolute;top:36px;width:429px;height:602px;background:var(--paper);border:1px solid var(--frame);overflow:hidden}
.flyer--retreat{left:36px}
.flyer--lodge{left:484px;width:428px}
.photo{position:absolute}
.body-text{font-family:'Kameron',serif;font-size:7.6px;line-height:1.38;color:var(--ink);text-align:justify}
.heading{font-family:'Oswald',sans-serif;font-weight:600;text-transform:uppercase;letter-spacing:.2px}
.heading span{color:var(--muted);font-weight:500}

/* Retreat flyer */
.retreat-hero{left:0;top:0;width:429px;height:306px;background:radial-gradient(ellipse at 45% 45%,#4b3a2a 0 12%,transparent 30%),linear-gradient(180deg,#3c3b1e 0%,#4e5a24 35%,var(--photo-green) 62%,#59452f 82%,#3e3022 100%)}
.brand-box{position:absolute;left:256px;top:60px;width:171px;height:54px;background:rgba(196,190,186,.86);display:flex;align-items:center;justify-content:center}
.brand-box__name{font-family:'Kameron',serif;font-size:19px;color:#3a3432;letter-spacing:1px}
.schedule{position:absolute;left:258px;top:267px;width:171px;height:335px;background:var(--taupe);padding:10px 12px 0;color:var(--paper)}
.schedule .heading{font-size:16px;text-align:center;color:var(--blush-text);line-height:1}
.schedule__intro{font-family:'Kameron',serif;font-size:6.6px;line-height:1.35;text-align:center;margin-top:6px;color:#f4efec}
.day{font-family:'Oswald',sans-serif;font-weight:600;font-size:12px;color:var(--blush-text);text-align:center;margin-top:7px;line-height:1}
.day-box{background:var(--blush);color:var(--taupe);font-family:'Kameron',serif;font-size:6px;line-height:1.4;text-align:center;padding:6px 4px;margin-top:5px}
.schedule .heading--retreats{margin-top:16px}
.about{position:absolute;left:14px;top:310px;width:238px}
.about .heading{font-size:17px;color:var(--ink);line-height:1}
.about .body-text{margin-top:7px}
.about .body-text + .body-text{margin-top:7px}
.strip{position:absolute;top:497px;height:38px}
.strip--left{left:14px;width:120px;background:linear-gradient(180deg,#2d5fa6 0%,#7aa5d6 45%,#6f7f5a 70%,#3f4a35 100%)}
.strip--right{left:134px;width:118px;background:linear-gradient(180deg,#b9cfe3 0%,#7f9a54 45%,#4f6a2c 100%)}
.contact{position:absolute;left:14px;top:540px;width:240px;height:52px;display:flex;align-items:center}
.contact .heading{font-size:14px;width:118px;padding-top:8px}
.divider{width:1px;height:50px;background:var(--ink);margin-right:6px}
.address{font-family:'Kameron',serif;font-size:7.3px;line-height:1.3;color:var(--ink)}
.address strong{font-size:9px;font-weight:700;display:block}

/* Lodge flyer */
.lodge-hero{left:0;top:0;width:428px;height:233px;background:linear-gradient(180deg,#eef1f2 0%,#dfe6e3 18%,#6f7d4a 32%,#3a2a1e 48%,#4a3424 66%,#a89378 82%,#c2b196 100%)}
.lodge-title{position:absolute;left:0;top:102px;width:428px;text-align:center;font-family:'Oswald',sans-serif;font-weight:300;font-size:34px;letter-spacing:3px;color:#f3f1ee;padding-right:36px}
.welcome{position:absolute;left:0;top:244px;width:428px;text-align:center}
.welcome__title{font-family:'Oswald',sans-serif;font-weight:600;font-size:17px;line-height:1.1;color:var(--ink);text-transform:uppercase}
.welcome__sub{font-family:'Oswald',sans-serif;font-weight:500;font-size:15.5px;line-height:1.1;color:var(--taupe-light);text-transform:uppercase}
.welcome__text{font-family:'Kameron',serif;font-size:9.8px;line-height:1.3;color:var(--ink);margin:5px auto 0;width:330px}
.card{position:absolute;top:335px;width:130px;height:219px;background:var(--taupe)}
.card--standard{left:7px}
.card--retreat{left:150px;width:129px}
.card--contact{left:293px;width:128px}
.card__photo{position:absolute;left:6px;top:8px;right:6px;height:95px}
.card--standard .card__photo{background:linear-gradient(180deg,#5a3a22 0%,#7b4a2a 40%,#2a2220 65%,#8a4a4a 100%)}
.card--retreat .card__photo{background:linear-gradient(180deg,#cdbfa3 0%,#bda98a 45%,#7b3f5a 70%,#e5dfe0 100%)}
.card--contact .card__photo{background:linear-gradient(180deg,#b27a44 0%,#d7a772 40%,#efe9e2 65%,#5a4a3a 100%)}
.card__label{position:absolute;left:0;right:0;top:106px;height:31px;background:var(--blush);font-family:'Oswald',sans-serif;font-weight:500;font-size:13px;color:var(--taupe);padding:7px 8px 0;text-transform:uppercase}
.card__text{position:absolute;left:6px;right:6px;top:145px;font-family:'Kameron',serif;font-size:6.7px;line-height:1.38;color:var(--paper);text-align:center}
.find{position:absolute;left:75px;top:560px;height:34px;display:flex;align-items:center}
.find .heading{font-size:15px;padding-right:10px}
.find .divider{height:26px;margin-right:8px}
.find .address{font-size:7.3px}
.find .address strong{display:inline;font-size:9px}
</style>
</head>
<body>
<main class="sheet">

  <section class="flyer flyer--retreat" aria-label="Velinos Haven yoga flyer">
    <div class="photo retreat-hero" role="img" aria-label="Photo of a woman seen from behind in a yoga pose, sitting on a tree stump in a green meadow"></div>
    <div class="brand-box"><span class="brand-box__name">VELINOS HAVEN</span></div>

    <div class="about">
      <h2 class="heading">About <span>Us</span></h2>
      <p class="body-text">Nullam posuere diam erat, non interdum libero consequat ac. Nam ut iaculis nunc, sed facilisis libero. Proin est sapien, varius eu diam nec, lacinia bibendum sem. Suspendisse eget convallis tortor, eget mattis sapien. Maecenas vulputate lectus non ante accumsan scelerisque. Curabitur laoreet pretium orci ut fermentum. Fusce euismod at justo vel pulvinar. Duis efficitur malesuada velit. Donec pretium, augue in imperdiet volutpat, erat ex vulputate quam, sit amet interdum urna metus a sapien.</p>
      <p class="body-text">Curabitur posuere lorem vel leo sodales rutrum. Morbi at tempor ligula, vehicula efficitur ante. Quisque vel vehicula mauris. Sed euismod libero ut nisl pharetra efficitur. Aenean eget nisl in tortor dictum euismod. Aenean</p>
    </div>

    <div class="photo strip strip--left" role="img" aria-label="Photo of a person in a yoga pose against a blue sky and hills"></div>
    <div class="photo strip strip--right" role="img" aria-label="Photo of a person meditating in a green valley"></div>

    <div class="contact">
      <h2 class="heading">Get in <span>touch!</span></h2>
      <div class="divider"></div>
      <p class="address"><strong>Velinos Haven</strong>12 Marrow Lakes<br>Elsworth. PE41 7QX<br>Tel: 01632 960 418<br>Mobile: 07700 900 173</p>
    </div>

    <aside class="schedule">
      <h2 class="heading">Our Schedules</h2>
      <p class="schedule__intro">Curabitur posuere lorem vel leo sodales rutrum. Morbi at tempor ligula, vehicula efficitur ante. Quisque vel vehicula</p>
      <h3 class="day">MONDAY</h3>
      <p class="day-box">Curabitur posuere lorem vel leo sodales rutrum. Morbi at tempor ligula, vehicula</p>
      <h3 class="day">TUESDAY</h3>
      <p class="day-box">Curabitur posuere lorem vel leo sodales rutrum. Morbi at tempor ligula, vehicula</p>
      <h3 class="day">FRIDAY</h3>
      <p class="day-box">Curabitur posuere lorem vel leo sodales rutrum. Morbi at tempor ligula, vehicula</p>
      <h2 class="heading heading--retreats">Retreats</h2>
      <p class="schedule__intro">Curabitur posuere lorem vel leo sodales rutrum. Morbi at tempor ligula, vehicula efficitur ante. Quisque vel vehicula mauris. Sed euismod libero ut nisl pharetra efficitur. Aenean eget nisl in</p>
    </aside>
  </section>

  <section class="flyer flyer--lodge" aria-label="Velinos Lodge cabin flyer">
    <div class="photo lodge-hero" role="img" aria-label="Photo of a dark log cabin with a red tiled roof and veranda among trees"></div>
    <p class="lodge-title">VELINOS LODGE</p>

    <div class="welcome">
      <h1 class="welcome__title">Welcome to the start of your getaway</h1>
      <p class="welcome__sub">In the heart of the English countryside</p>
      <p class="welcome__text">If you are looking to escape to the country for a short break, then our modern, spacious cabin in the heart of Norfolk could be exactly what you are looking for</p>
    </div>

    <article class="card card--standard">
      <div class="card__photo" role="img" aria-label="Photo of the cabin living room with leather sofas and a striped rug"></div>
      <h3 class="card__label">Standard</h3>
      <p class="card__text">If you wish to find out more about the Cabin and wish to create your holiday in the idyllic Norfolk countryside with us, then please get in touch via the form below.</p>
    </article>
    <article class="card card--retreat">
      <div class="card__photo" role="img" aria-label="Photo of the cabin bedroom with a double bed and striped throw"></div>
      <h3 class="card__label">Retreat</h3>
      <p class="card__text">The Cabin can sleep up to 8 people and is booked in week slots in the summer months; however, shorter breaks can be arranged outside of peak season upon request.</p>
    </article>
    <article class="card card--contact">
      <div class="card__photo" role="img" aria-label="Photo of the cabin bathroom with a freestanding bath under a wooden ceiling"></div>
      <h3 class="card__label">Contact</h3>
      <p class="card__text">We aim to get back to you within 72 hours of your enquiry through the site. Or for an immediate response, please get in touch direct via phone or email.</p>
    </article>

    <div class="find">
      <h2 class="heading">Find<span>us!</span></h2>
      <div class="divider"></div>
      <p class="address"><strong>Velinos Lodge</strong> - 12 Marrow Lakes - Elsworth. PE41 7QX<br>Tel: 01632 960 418 - Mobile: 07700 900 173</p>
    </div>
  </section>

</main>
</body>
</html>
```